Business Card Design for a Sound engineer and DJ

We would like a residn of the business card.

Logo must remain the same.
The card is for the owner of the company.
The business card is in Arabic as the company is based in Kuwait.
The company specializes in sound engineering for singers concerts and events and in addition DJ.
The color options is up to the designer but we would like it masculine as the owner is a man.

Target Market(s)

All ages

Industry/Entity Type

Media

Contact Information for Business Card

Name:
Eng. Faisal Barrak
م/فيصل براك

The name above is in Arabic and English.

Title: General Manager
Mobile: +965 96370482
Office: +965 22480637
Email: info@qamarwave.net

Address:
Office no. 3
1st floor
Marjan Complex
Hamad Faraj St.
Salmiya
Kuwait

Instagram: @qamarwave
Snap: qamarwave

Requirements
Nice to have
• can we have Instagram icon and snap icon and a phone vector and email?
• Instead of writing the words

```html
<!DOCTYPE html>
<html lang="en">
<head>
<meta charset="utf-8">
<title>Qamar Wave — Business Card</title>
<link rel="stylesheet" href="https://fonts.googleapis.com/css2?family=Open+Sans:wght@400;600&family=Noto+Kufi+Arabic:wght@500&family=Noto+Naskh+Arabic:wght@500&display=swap">
<style>
  :root {
    --page: #e9e6cf;
    --card-back: #6474b8;
    --card-back-rule: #8b3d9c;
    --card-front: #f8f9fb;
    --card-front-rule: #5866b4;
    --ink-blue: #5866b4;
    --ink-purple: #7d2d8e;
    --ink-white: #ffffff;
    --brand-pink: #c2419a;
  }
  * { margin: 0; padding: 0; box-sizing: border-box; }
  html, body { width: 1200px; height: 1200px; overflow: hidden; }
  body {
    background: var(--page);
    font-family: "Open Sans", "Noto Naskh Arabic", sans-serif;
    position: relative;
  }
  .card {
    position: absolute;
    left: 150px;
    width: 900px;
    height: 514px;
    border-radius: 46px;
  }
  .card__rule {
    position: absolute;
    inset: 20px;
    border-radius: 34px;
    border: 2px solid;
  }
  /* back side */
  .card--back { top: 60px; background: var(--card-back); }
  .card--back .card__rule { border-color: var(--card-back-rule); }
  .brand {
    position: absolute;
    display: flex;
    flex-direction: column;
  }
  .brand--back { left: 190px; top: 178px; align-items: flex-start; }
  .brand__mark {
    width: 92px; height: 92px;
    background: var(--brand-pink);
    position: absolute;
  }
  .brand--back .brand__mark { left: 0; top: 20px; }
  .brand--back .brand__text { margin-left: 122px; color: var(--ink-white); }
  .brand__name {
    font-weight: 600;
    letter-spacing: 0.18em;
    text-transform: uppercase;
    line-height: 1.1;
  }
  .brand--back .brand__name { font-size: 50px; }
  .brand__tag {
    font-weight: 600;
    letter-spacing: 0.12em;
    text-transform: uppercase;
  }
  .brand--back .brand__tag { font-size: 19px; margin-top: 6px; }
  .brand__tag-ar {
    font-family: "Noto Kufi Arabic", sans-serif;
    direction: rtl;
    text-align: left;
  }
  .brand--back .brand__tag-ar { font-size: 19px; margin-top: 2px; }

  /* front side */
  .card--front { top: 626px; background: var(--card-front); }
  .card--front .card__rule { border-color: var(--card-front-rule); }
  .brand--front { left: 66px; top: 70px; color: var(--ink-purple); }
  .brand--front .brand__mark { position: static; width: 70px; height: 70px; margin-bottom: 26px; }
  .brand--front .brand__name { font-size: 34px; }
  .brand--front .brand__tag { font-size: 14px; margin-top: 4px; color: var(--ink-blue); }
  .brand--front .brand__tag-ar { font-size: 14px; color: var(--ink-purple); }

  .owner {
    position: absolute;
    right: 62px; top: 74px;
    text-align: right;
  }
  .owner__name { font-size: 34px; color: var(--ink-purple); line-height: 1.2; }
  .owner__name-ar {
    font-family: "Noto Naskh Arabic", serif;
    font-size: 28px; color: var(--ink-purple);
    direction: rtl; line-height: 1.3;
  }
  .owner__title { font-size: 21px; color: var(--ink-blue); letter-spacing: 0.02em; }

  .contact {
    position: absolute;
    right: 62px; top: 280px;
    list-style: none;
    color: var(--ink-blue);
    font-size: 22px;
  }
  .contact__item { display: flex; justify-content: flex-end; align-items: center; gap: 14px; line-height: 32px; }
  .contact__icon { width: 22px; height: 22px; fill: none; stroke: var(--ink-blue); stroke-width: 2; }

  .address {
    position: absolute;
    right: 62px; top: 392px;
    text-align: right;
    font-style: normal;
    color: var(--ink-blue);
    font-size: 21px;
    line-height: 29px;
  }
  .social {
    position: absolute;
    left: 60px; top: 386px;
    list-style: none;
    color: var(--ink-blue);
    font-size: 22px;
  }
  .social__item { display: flex; align-items: center; gap: 12px; line-height: 32px; }
  .social__dot { width: 18px; height: 18px; border-radius: 50%; background: var(--ink-blue); }
</style>
</head>
<body>

<section class="card card--back" aria-label="Card back">
  <div class="card__rule"></div>
  <div class="brand brand--back">
    <span class="brand__mark"></span>
    <div class="brand__text">
      <p class="brand__name">Qamar Wave</p>
      <p class="brand__tag">DJ - Sound Eng. - Lighting</p>
      <p class="brand__tag-ar" lang="ar">دي جي - هندسة صوت - إضاءة</p>
    </div>
  </div>
</section>

<section class="card card--front" aria-label="Card front">
  <div class="card__rule"></div>

  <div class="brand brand--front">
    <span class="brand__mark"></span>
    <p class="brand__name">Qamar Wave</p>
    <p class="brand__tag">DJ - Sound Eng. - Lighting</p>
    <p class="brand__tag-ar" lang="ar">دي جي - هندسة صوت - إضاءة</p>
  </div>

  <div class="owner">
    <p class="owner__name">Eng. Faisal Barrak</p>
    <p class="owner__name-ar" lang="ar">م/فيصل براك</p>
    <p class="owner__title">General Manager</p>
  </div>

  <ul class="contact">
    <li class="contact__item">+965 96370482
      <svg class="contact__icon" viewBox="0 0 22 22"><rect x="6" y="2" width="10" height="18" rx="2"/><line x1="10" y1="17" x2="12" y2="17"/></svg>
    </li>
    <li class="contact__item">+965 22480637
      <svg class="contact__icon" viewBox="0 0 22 22"><path d="M3 9c0-3 16-3 16 0v2h-4V9H7v2H3z"/><rect x="5" y="12" width="12" height="7" rx="1"/></svg>
    </li>
    <li class="contact__item">info@qamarwave.net
      <svg class="contact__icon" viewBox="0 0 22 22"><rect x="2" y="5" width="18" height="13"/><polyline points="2,5 11,12 20,5"/></svg>
    </li>
  </ul>

  <address class="address">
    Office no. 3, 1st floor<br>
    Marjan Complex<br>
    Hamad Faraj St., Salmiya, Kuwait
  </address>

  <ul class="social">
    <li class="social__item"><span class="social__dot"></span>Instagram @qamarwave</li>
    <li class="social__item"><span class="social__dot"></span>Snap qamarwave</li>
  </ul>
</section>

</body>
</html>
```